Create a Branded Excel Invoice for a Jewellery Company

Hi,

I need an invoice template created for a jewelry company. The invoice must have a color scheme that matches the logo. I attached a sample invoice below, this is only for REFERENCE so that you know what fields should be in the invoice.

For all the fields refer to the sample invoice I attached. The content should be the same but the actual color and layout can be different.

-Color must match the logo
-Must have branding
-Must be a consistent color scheme
-Must have all the fields as in the invoice example
-Use placeholder text until awarded entry
-Must be in EXCEL format

I will rate all the entries, please stay away from ideas that get less than 3 stars.

```html
<!DOCTYPE html>
<html lang="en">
<head>
<meta charset="utf-8">
<title>Invoice 0051 – Lumen Jewellery</title>
<link rel="stylesheet" href="https://fonts.googleapis.com/css2?family=Arimo:wght@400;700&display=swap">
<style>
  :root {
    --gold: #c48f58;
    --rule: #c9a273;
    --fill: #f7e0cb;
    --ink: #1e1e1e;
    --paper: #ffffff;
  }
  * { box-sizing: border-box; margin: 0; padding: 0; }
  html, body { width: 1200px; height: 1055px; overflow: hidden; background: var(--paper); }
  body { position: relative; font-family: "Arimo", Arial, sans-serif; color: var(--ink); font-size: 18px; }

  .brand { position: absolute; left: 24px; top: 168px; display: flex; align-items: center; gap: 12px; }
  .brand-dot { width: 18px; height: 18px; border-radius: 50%; background: var(--gold); }
  .brand-name { font-family: "Arimo", Arial, sans-serif; font-weight: 400; font-size: 34px; letter-spacing: 2px; color: var(--gold); line-height: 1; }

  .doc-title { position: absolute; right: 40px; top: 74px; font-size: 74px; font-weight: 700; color: var(--gold); line-height: 1; letter-spacing: 1px; }

  .rule { position: absolute; left: 24px; width: 1154px; height: 3px; background: var(--rule); }
  .rule-top { top: 151px; }
  .rule-mid { top: 322px; height: 2px; }

  .meta { position: absolute; top: 191px; left: 700px; display: grid; grid-template-columns: 228px auto; column-gap: 8px; row-gap: 5px; line-height: 22px; }
  .meta dt, .party-label, .totals-label { color: var(--gold); font-weight: 700; text-align: right; }

  .party { position: absolute; top: 374px; display: grid; grid-template-columns: auto auto; column-gap: 7px; line-height: 24.5px; }
  .party address { font-style: normal; }
  .party-from { left: 110px; }
  .party-for { left: 650px; }

  .items { position: absolute; left: 24px; top: 525px; width: 1154px; border-collapse: collapse; table-layout: fixed; }
  .items th { color: var(--gold); font-weight: 700; text-align: left; height: 26px; padding: 0 4px; border-bottom: 3px solid var(--rule); vertical-align: top; }
  .items th.col-amount { text-align: right; padding-right: 6px; }
  .items td { height: 27.7px; border: 1.5px solid var(--rule); padding: 0 8px 0 20px; white-space: nowrap; }
  .items td.col-desc { padding-left: 22px; }
  .items td.col-qty { text-align: right; padding-right: 12px; }
  .items td.col-amount { background: var(--fill); }
  .money { display: flex; justify-content: space-between; }
  .items td.col-price, .items td.col-amount { padding-left: 18px; padding-right: 10px; }

  .totals { position: absolute; left: 760px; top: 773px; border-collapse: collapse; }
  .totals td { height: 27.7px; }
  .totals-label { width: 165px; padding-right: 6px; }
  .totals-value { width: 250px; background: var(--fill); border: 1.5px solid var(--rule); padding: 0 10px 0 28px; }

  .thanks { position: absolute; left: 0; width: 1200px; top: 1004px; text-align: center; color: var(--gold); font-weight: 700; font-size: 23px; }
  .contact { position: absolute; left: 0; width: 1200px; top: 1034px; text-align: center; font-size: 17px; }
</style>
</head>
<body>
  <header>
    <div class="brand">
      <span class="brand-dot"></span>
      <span class="brand-name">LUMEN JEWELLERY</span>
    </div>
    <h1 class="doc-title">INVOICE</h1>
  </header>
  <div class="rule rule-top"></div>

  <dl class="meta">
    <dt>Invoice ID:</dt><dd>0051</dd>
    <dt>Issue Date:</dt><dd>06/05/2017</dd>
    <dt>Due Date:</dt><dd>06/05/2017 (upon receipt)</dd>
    <dt>Subject:</dt><dd>Spring Marketing Campaign</dd>
  </dl>
  <div class="rule rule-mid"></div>

  <div class="party party-from">
    <span class="party-label">From</span>
    <address>Northfield Studio<br>12 Harrow Lane<br>Dunmore D4 7QL<br>Westland</address>
  </div>
  <div class="party party-for">
    <span class="party-label">For</span>
    <address>Kestrel Press<br>58 Orchard Row<br>Ashby AB2 9TR<br>Eastmoor</address>
  </div>

  <table class="items">
    <colgroup><col style="width:147px"><col style="width:527px"><col style="width:90px"><col style="width:139px"><col style="width:251px"></colgroup>
    <thead>
      <tr><th>Item Type</th><th style="padding-left:9px">Description</th><th>Quantity</th><th style="padding-left:20px">Unit Price</th><th class="col-amount">Amount</th></tr>
    </thead>
    <tbody>
      <tr><td>Service</td><td class="col-desc">Design</td><td class="col-qty">41</td><td class="col-price"><span class="money"><span>$</span><span>230.00</span></span></td><td class="col-amount"><span class="money"><span>$</span><span>9,430.00</span></span></td></tr>
      <tr><td>Service</td><td class="col-desc">Development</td><td class="col-qty">57</td><td class="col-price"><span class="money"><span>$</span><span>330.00</span></span></td><td class="col-amount"><span class="money"><span>$</span><span>18,810.00</span></span></td></tr>
      <tr><td>Service</td><td class="col-desc">Meeting</td><td class="col-qty">5</td><td class="col-price"><span class="money"><span>$</span><span>60.00</span></span></td><td class="col-amount"><span class="money"><span>$</span><span>270.00</span></span></td></tr>
      <tr><td></td><td></td><td></td><td></td><td class="col-amount"></td></tr>
      <tr><td></td><td></td><td></td><td></td><td class="col-amount"></td></tr>
      <tr><td></td><td></td><td></td><td></td><td class="col-amount"></td></tr>
      <tr><td></td><td></td><td></td><td></td><td class="col-amount"></td></tr>
    </tbody>
  </table>

  <table class="totals">
    <tr><td class="totals-label">Subtotal</td><td class="totals-value"><span class="money"><span>$</span><span>28,510.00</span></span></td></tr>
    <tr><td class="totals-label">Tax 10%</td><td class="totals-value"><span class="money"><span>$</span><span>2,851.00</span></span></td></tr>
    <tr><td class="totals-label">Payment</td><td class="totals-value"><span class="money"><span>$</span><span>(31,361.00)</span></span></td></tr>
    <tr><td class="totals-label">Amount Due</td><td class="totals-value"><span class="money"><span>$</span><span>-&nbsp;&nbsp;&nbsp;&nbsp;</span></span></td></tr>
  </table>

  <footer>
    <p class="thanks">Thank you for your business!</p>
    <p class="contact">Street Address, City, ST&nbsp; ZIP Code,&nbsp; Phone,&nbsp; Fax,&nbsp; E-mail</p>
  </footer>
</body>
</html>
```